731 Orchard Avenue Residences

designing a sign for apartment complex;
prefer colors gray white and yellow

Target Market(s)

residents coming home to their apartment

Font styles to use
Serif
Sans Serif

Colors
FFF300
FFF600
FEFA6F
FFFEC7
FFFEE8

Requirements
Must have
• black or gray, white and some yellow; easy to read and see

```html
<!DOCTYPE html>
<html lang="en">
<head>
<meta charset="utf-8">
<title>Welcome Sign Concepts</title>
<link rel="stylesheet" href="https://fonts.googleapis.com/css2?family=Playfair+Display:wght@900&family=Montserrat:wght@300;600&display=swap">
<style>
  :root {
    --yellow: #FFF300;
    --yellow-deep: #FFD400;
    --yellow-soft: #FEFA6F;
    --cream: #FFFEE8;
    --gray: #6B6B6B;
    --gray-light: #E6E8EC;
    --gray-mid: #9A9A9A;
    --ink: #111111;
    --paper: #FFFFFF;
  }
  html, body {
    margin: 0;
    padding: 0;
    width: 1200px;
    height: 2529px;
    overflow: hidden;
    background: var(--paper);
  }
  .canvas {
    position: relative;
    width: 1200px;
    height: 2529px;
  }
  .sign-art {
    position: absolute;
    left: 0;
    top: 0;
  }
  .brand-word {
    font-family: "Playfair Display", Georgia, serif;
    font-weight: 900;
    fill: var(--ink);
  }
  .welcome-line {
    font-family: "Montserrat", Arial, sans-serif;
    font-weight: 300;
    fill: var(--ink);
  }
  .caption {
    position: absolute;
    left: 0;
    top: 912px;
    width: 1200px;
    margin: 0;
    text-align: center;
    font-family: "Montserrat", Arial, sans-serif;
    font-weight: 600;
    font-size: 15px;
    line-height: 21px;
    color: var(--ink);
  }
</style>
</head>
<body>
<div class="canvas">
  <svg class="sign-art" width="1200" height="2529" viewBox="0 0 1200 2529" xmlns="http://www.w3.org/2000/svg">
    <defs>
      <linearGradient id="swoosh-yellow" x1="0" y1="0" x2="1" y2="0">
        <stop offset="0" stop-color="#FFF300"/>
        <stop offset="0.6" stop-color="#FFD400"/>
        <stop offset="1" stop-color="#FFFEC7"/>
      </linearGradient>
    </defs>

    <!-- Concept 1: portrait sign with yellow name band -->
    <g class="sign sign--band">
      <path class="sign-frame" d="M230 135 Q430 70 625 135 L625 735 L230 735 Z" fill="var(--gray-light)"/>
      <path class="sign-face" d="M250 150 Q430 105 602 150 L602 713 L250 713 Z" fill="var(--paper)"/>
      <circle class="brand-dot" cx="432" cy="327" r="68" fill="var(--yellow-deep)"/>
      <rect class="name-band" x="250" y="412" width="352" height="150" fill="var(--yellow)"/>
      <text class="brand-word" x="432" y="488" font-size="66" text-anchor="middle">Brand</text>
      <text class="brand-word" x="432" y="540" font-size="66" text-anchor="middle">name</text>
      <text class="welcome-line" x="432" y="593" font-size="16" text-anchor="middle">welcome back to</text>
      <text class="welcome-line" x="432" y="611" font-size="16" text-anchor="middle">your apartment</text>
      <circle class="welcome-ring" cx="432" cy="638" r="14" fill="none" stroke="var(--yellow-deep)" stroke-width="2"/>
    </g>

    <!-- Concept 2: portrait sign with swooshes -->
    <g class="sign sign--swoosh">
      <path class="sign-frame" d="M240 1150 Q435 1085 630 1150 L630 1740 L240 1740 Z" fill="var(--gray-light)"/>
      <path class="sign-face" d="M258 1165 Q435 1120 610 1165 L610 1718 L258 1718 Z" fill="var(--paper)"/>
      <path class="swoosh-yellow" d="M258 1165 L355 1145 Q360 1330 258 1465 Z" fill="url(#swoosh-yellow)"/>
      <path class="swoosh-gray" d="M610 1500 Q565 1600 576 1718 L610 1718 Z" fill="var(--gray)"/>
      <circle class="brand-dot" cx="440" cy="1340" r="68" fill="var(--yellow-deep)"/>
      <text class="brand-word" x="445" y="1503" font-size="66" text-anchor="middle">Brand</text>
      <text class="brand-word" x="445" y="1553" font-size="66" text-anchor="middle">name</text>
      <text class="welcome-line" x="442" y="1600" font-size="16" text-anchor="middle">welcome back to</text>
      <text class="welcome-line" x="442" y="1618" font-size="16" text-anchor="middle">your apartment</text>
      <circle class="welcome-ring" cx="440" cy="1644" r="14" fill="none" stroke="var(--yellow-deep)" stroke-width="2"/>
    </g>

    <!-- Concept 3: low monument sign -->
    <g class="sign sign--monument">
      <rect class="monument-base" x="373" y="2350" width="490" height="125" fill="var(--gray-mid)"/>
      <rect class="monument-plinth" x="367" y="2468" width="502" height="14" fill="#8A8A8A"/>
      <rect class="monument-stripe" x="387" y="2330" width="460" height="20" fill="var(--yellow)"/>
      <path class="monument-face" d="M370 2085 L850 2085 L865 2235 L865 2330 L370 2330 Z" fill="var(--paper)"/>
      <path class="monument-gray" d="M385 2085 L850 2090 L850 2232 Q700 2120 385 2117 Z" fill="var(--gray-mid)"/>
      <path class="monument-yellow" d="M385 2085 L720 2088 Q560 2090 385 2095 Z M385 2117 Q700 2115 850 2235 Q700 2130 385 2122 Z" fill="var(--yellow-deep)"/>
      <circle class="brand-dot" cx="620" cy="2204" r="44" fill="var(--yellow-deep)"/>
      <text class="brand-word" x="622" y="2290" font-size="38" text-anchor="middle">Brand name</text>
      <text class="welcome-line" x="615" y="2304" font-size="9" text-anchor="middle">welcome back to your apartment</text>
      <circle class="welcome-ring" cx="702" cy="2301" r="4.5" fill="none" stroke="var(--yellow-deep)" stroke-width="1"/>
    </g>
  </svg>

  <p class="caption">simple but clever and professional sign for apartment complex welcoming<br>residents who are coming back to their apartments</p>
</div>
</body>
</html>
```